Fernvale Craft Works business card design- Fine Art sculpture business (Contract guaranteed)

This business card is for a fine art business. Though we don't have a website up and running yet it should be up soon. I would like the business card to be elegant and fairly simple with a picture of one of my sculptures on the front (you might need to photoshop out the background) as well as my basic contact info (my name,phone # and e-mail). On the back I'd like it to be pretty simple with just "Notes" and some blank lines for writing in info.

Target Market(s)

High end artwork buyers

Industry/Entity Type

Art Gallery

Contact Information for Business Card

Marlo Prewitt Phone: (555) 213-4098 E-mail: marlo@quillbrookmail.com Facebook: @fernvalecraftworks Instagram: fernvalecraftworks

Colors

Designer to choose colors to be used in the design.

Requirements
Must have
• *A picture of one of my sculptures*, my name, business name (Fernvale Craft Works), e-mail, phone #, and a notes section on the back.
• Fernvale Craft Works
• Marlo Prewitt
• (555)213-4098
• marlo@quillbrookmail.com
• Facebook: @fernvalecraftworks
• Instagram: fernvalecraftworks
Nice to have
• It'd be nice if you can crop out the background in the sculpture pictures, which ever one you end up using.

```html
<!DOCTYPE html>
<html lang="en">
<head>
<meta charset="utf-8">
<title>Fernvale Craft Works – Business Card</title>
<link href="https://fonts.googleapis.com/css2?family=Open+Sans:wght@400;600;700&display=swap" rel="stylesheet">
<style>
  :root {
    --purple: #5e3489;
    --ink: #111111;
    --paper: #ffffff;
    --backdrop: #f4f4f4;
    --soft-text: #f1ecf7;
    --stone-dark: #1f4a33;
    --stone-light: #4f9a70;
  }
  * { margin: 0; padding: 0; box-sizing: border-box; }
  html, body {
    width: 1200px; height: 1200px; overflow: hidden;
    background: var(--backdrop);
    font-family: "Open Sans", Arial, sans-serif;
  }
  .card {
    position: absolute; left: 160px; width: 859px; height: 500px;
    background: var(--paper); overflow: hidden;
  }
  .card--back { top: 80px; }
  .card--front { top: 614px; }

  /* Notes side */
  .brand-mini {
    position: absolute; top: 30px; left: 0; width: 100%;
    display: flex; justify-content: center; align-items: center; gap: 8px;
    font-weight: 700; font-size: 20px; color: var(--ink);
  }
  .brand-mini .dot { width: 16px; height: 16px; border-radius: 50%; background: var(--purple); }
  .brand-mini-tagline {
    position: absolute; top: 68px; left: 0; width: 100%; text-align: center;
    font-size: 7px; letter-spacing: 0.5px; color: var(--ink);
  }
  .notes-title {
    position: absolute; top: 104px; left: 0; width: 100%; text-align: center;
    font-weight: 700; font-size: 39px; color: var(--purple); letter-spacing: 1px;
  }
  .notes-lines { position: absolute; left: 0; top: 0; }

  /* Front side */
  .purple-panel { position: absolute; inset: 0; }
  .sculpture-ghost {
    position: absolute; left: 110px; top: 0; width: 180px; height: 470px;
    background: linear-gradient(180deg, #dfe6e1, #e9ede9 60%, #dcdcdc);
    opacity: 0.6; border-radius: 40% 30% 20% 20%;
  }
  .studio-name {
    position: absolute; left: 34px; top: 52px;
    font-weight: 700; font-size: 31px; color: var(--purple); letter-spacing: 0.5px;
  }
  .brand-large {
    position: absolute; left: 40px; top: 180px; width: 380px;
    display: flex; align-items: center; gap: 16px;
    font-weight: 700; font-size: 54px; line-height: 1.05; color: var(--ink);
  }
  .brand-large .dot { flex: none; width: 46px; height: 46px; border-radius: 50%; background: var(--purple); }
  .tagline-rule {
    position: absolute; left: 37px; top: 376px; width: 352px;
    display: flex; align-items: center; gap: 6px;
    font-size: 11px; color: var(--ink); white-space: nowrap;
  }
  .tagline-rule::before, .tagline-rule::after { content: ""; flex: 1; height: 1px; background: #555; }
  .sculpture-photo {
    position: absolute; left: 592px; top: 30px; width: 100px; height: 272px;
    background: linear-gradient(180deg, var(--stone-light), var(--stone-dark) 70%, #1a1a1a);
    border-radius: 40% 50% 20% 20%;
  }
  .owner-name {
    position: absolute; left: 490px; top: 300px;
    font-weight: 700; font-size: 31px; color: var(--soft-text); letter-spacing: 0.5px;
  }
  .owner-rule { position: absolute; left: 490px; top: 336px; width: 230px; height: 1px; background: var(--soft-text); }
  .contact {
    position: absolute; left: 488px; display: flex; align-items: center; gap: 20px;
    font-weight: 600; font-size: 17px; color: var(--paper);
  }
  .contact--phone { top: 352px; }
  .contact--email { top: 394px; }
  .contact .icon { width: 36px; height: 36px; }
</style>
</head>
<body>

<section class="card card--back">
  <div class="brand-mini"><span class="dot"></span>The Quarry Folk</div>
  <div class="brand-mini-tagline">EVERY STONE TELLS A STORY</div>
  <h2 class="notes-title">NOTES SECTION</h2>
  <svg class="notes-lines" width="859" height="500" aria-hidden="true">
    <g stroke="#111" stroke-width="2">
      <line x1="0" y1="158" x2="859" y2="158"/>
      <line x1="0" y1="189" x2="859" y2="189"/>
      <line x1="0" y1="220" x2="859" y2="220"/>
      <line x1="0" y1="245" x2="859" y2="245"/>
      <line x1="0" y1="273" x2="859" y2="273"/>
      <line x1="0" y1="303" x2="859" y2="303"/>
      <line x1="0" y1="333" x2="859" y2="333"/>
      <line x1="0" y1="365" x2="859" y2="365"/>
      <line x1="0" y1="398" x2="859" y2="398"/>
      <line x1="0" y1="430" x2="859" y2="430"/>
    </g>
  </svg>
</section>

<section class="card card--front">
  <div class="sculpture-ghost" role="img" aria-label="Faint background photo of a green stone sculpture on a round base"></div>
  <svg class="purple-panel" width="859" height="500" aria-hidden="true">
    <polygon points="484,0 859,0 859,500 381,500" fill="var(--purple)"/>
  </svg>
  <h1 class="studio-name">FERNVALE CRAFT WORKS</h1>
  <div class="brand-large"><span class="dot"></span><span>The Quarry Folk</span></div>
  <div class="tagline-rule">EVERY STONE TELLS A STORY, EVERY PIECE</div>
  <div class="sculpture-photo" role="img" aria-label="Photo of a polished green malachite sculpture on a round dark base"></div>
  <div class="owner-name">MARLO PREWITT</div>
  <div class="owner-rule"></div>
  <div class="contact contact--phone">
    <svg class="icon" viewBox="0 0 36 36" aria-hidden="true">
      <circle cx="18" cy="18" r="18" fill="#000"/>
      <path d="M12 9c1.5-.8 2.6.2 3.4 1.8l1 2.2c.4 1-.1 1.8-.9 2.4l-.9.7c.8 2 2.4 3.8 4.4 4.9l.8-.9c.7-.7 1.5-1 2.4-.5l2.2 1.2c1.5.8 2.3 2 1.4 3.4-1 1.6-2.7 2.4-4.6 1.8C15.5 24.3 11 19.6 9.8 14c-.4-2 .5-3.9 2.2-5z" fill="#fff"/>
    </svg>
    <span>(555) 213-4098</span>
  </div>
  <div class="contact contact--email">
    <svg class="icon" viewBox="0 0 36 36" aria-hidden="true">
      <circle cx="18" cy="18" r="18" fill="#000"/>
      <rect x="9" y="11.5" width="18" height="13" fill="#fff"/>
      <polyline points="9,11.5 18,19 27,11.5" fill="none" stroke="#000" stroke-width="1.4"/>
      <line x1="9" y1="24.5" x2="15.5" y2="17" stroke="#000" stroke-width="1.2"/>
      <line x1="27" y1="24.5" x2="20.5" y2="17" stroke="#000" stroke-width="1.2"/>
    </svg>
    <span>marlo@quillbrookmail.com</span>
  </div>
</section>

</body>
</html>
```